Whistling Pebblefinch Coffee Co menu

We would like our existing menu tidied up.
we want to keep the all the items, but need it less busy and clearer to read.

Also want to leave a bit of space to add a few item in the future.

```html
<!DOCTYPE html>
<html lang="en">
<head>
<meta charset="utf-8">
<title>Whistling Pebblefinch Coffee Co — Menu</title>
<link rel="stylesheet" href="https://fonts.googleapis.com/css2?family=Arimo:wght@400;700&family=Rye&display=swap">
<style>
  :root {
    --ink: #111111;
    --paper: #ffffff;
    --motif: #ebebeb;
  }
  * { box-sizing: border-box; margin: 0; padding: 0; }
  html, body { width: 777px; height: 1200px; overflow: hidden; background: var(--paper); }
  body { font-family: "Arimo", Arial, sans-serif; color: var(--ink); }
  .menu { position: relative; width: 777px; height: 1200px; overflow: hidden; }

  .motif {
    position: absolute; left: 40px; top: 120px; width: 700px; height: 820px;
    background: radial-gradient(ellipse at 55% 50%, var(--motif) 0%, rgba(235,235,235,0.6) 45%, rgba(255,255,255,0) 72%);
  }

  .brand {
    position: absolute; left: 43px; top: 62px; width: 300px;
    display: flex; align-items: center; gap: 12px;
  }
  .brand-dot { width: 22px; height: 22px; border-radius: 50%; background: var(--ink); flex: none; }
  .brand-name { font-size: 24px; font-weight: 700; line-height: 1.15; }

  .page-title {
    position: absolute; left: 430px; top: 40px; width: 310px; text-align: center;
    font-family: "Rye", serif; line-height: 1;
  }
  .page-title .big { display: block; font-size: 58px; letter-spacing: 1px; }
  .page-title .small { display: block; font-size: 30px; margin-top: 2px; }

  .rule { position: absolute; height: 3px; background: var(--ink); }

  .section-label {
    position: absolute; font-size: 18px; font-weight: 700;
    text-decoration: underline; text-decoration-thickness: 2px; text-underline-offset: 3px;
  }

  .item { position: absolute; }
  .col-left .item { left: 43px; width: 320px; }
  .col-right .item { left: 427px; width: 308px; }
  .item-head { display: flex; justify-content: space-between; align-items: baseline; }
  .item-name { font-size: 19px; font-weight: 700; }
  .item-price { font-size: 12px; font-weight: 700; }
  .item-desc { font-size: 11.2px; line-height: 17.8px; margin-top: 5px; }

  .specials-title {
    position: absolute; left: 0; top: 826px; width: 777px; text-align: center;
    font-family: "Rye", serif; font-size: 36px;
  }
  .special { position: absolute; left: 60px; width: 657px; text-align: center; }
  .special-name { font-size: 19px; font-weight: 700; }
  .special-desc { font-size: 11.2px; line-height: 17.8px; margin-top: 9px; }
  .special-price { font-size: 12px; font-weight: 700; margin-top: 14px; }
</style>
</head>
<body>
<main class="menu">
  <div class="motif" role="img" aria-label="Faint large coffee leaf and bean decoration"></div>

  <header>
    <div class="brand">
      <span class="brand-dot"></span>
      <span class="brand-name">Whistling Pebblefinch Coffee Co</span>
    </div>
    <h1 class="page-title"><span class="big">COFFEE</span><span class="small">&amp; TEA</span></h1>
  </header>

  <div class="rule" style="left:43px; top:178px; width:309px;"></div>
  <div class="rule" style="left:427px; top:178px; width:308px;"></div>

  <section class="col-left">
    <h2 class="section-label" style="left:43px; top:198px;">Coffee&nbsp;&nbsp;</h2>

    <div class="item" style="top:234px;">
      <div class="item-head"><span class="item-name">Flat White</span><span class="item-price">$5.00</span></div>
      <p class="item-desc">Espresso Shot With A Steamed Milk.<br>Small $5 - Medium $6 - Large $7</p>
    </div>
    <div class="item" style="top:309px;">
      <div class="item-head"><span class="item-name">Cappuccino</span><span class="item-price">$5.00</span></div>
      <p class="item-desc">Espresso Shot With Steamed Milk, A Thick Layer<br>Of Milk Foam And Chocolate Powder Topping.<br>Small $5 - Medium $6 - Large $7</p>
    </div>
    <div class="item" style="top:400px;">
      <div class="item-head"><span class="item-name">Latte</span><span class="item-price">$5.00</span></div>
      <p class="item-desc">Espresso Shot With Steamed Milk And A Thin<br>Layer Of Milk Foam<br>Small $5 - Medium $6 - Large $7</p>
    </div>
    <div class="item" style="top:491px;">
      <div class="item-head"><span class="item-name">Mocha</span><span class="item-price">$5.50</span></div>
      <p class="item-desc">Espresso Shot, Belgian Chocolate Raw Natural<br>Infusion With A Medium Layer Of Milk Foam.<br>Small $5 - Medium $6 - Large $7</p>
    </div>
    <div class="item" style="top:582px; width:330px;">
      <div class="item-head" style="width:320px;"><span class="item-name">Americano</span><span class="item-price">$5.00</span></div>
      <p class="item-desc">Americano - Espresso Shot Topped Up With Hot Water.<br>Long Black - Hot Water Topped Off With Espresso Shot<br>Small $5 - Medium $6 - Large $7</p>
    </div>
    <div class="item" style="top:673px;">
      <div class="item-head"><span class="item-name">Espresso</span><span class="item-price">$3.00</span></div>
      <p class="item-desc">Double Espresso Shot</p>
    </div>
    <div class="item" style="top:729px;">
      <div class="item-head"><span class="item-name">Filter / Batch Brew Coffee</span><span class="item-price">$4.00</span></div>
      <p class="item-desc">Small $4 - Medium $4 - Large $4</p>
    </div>
  </section>

  <section class="col-right">
    <h2 class="section-label" style="left:427px; top:198px;">Tea / Other drinks&nbsp;&nbsp;</h2>

    <div class="item" style="top:235px;">
      <div class="item-head"><span class="item-name">Organic Green Tea</span><span class="item-price">$5.00</span></div>
      <p class="item-desc">Small $5 - Medium $6 - Large $7</p>
    </div>
    <div class="item" style="top:291px;">
      <div class="item-head"><span class="item-name">English Breakfast Tea</span><span class="item-price">$5.00</span></div>
      <p class="item-desc">Small $5 - Medium $6 - Large $7</p>
    </div>
    <div class="item" style="top:348px;">
      <div class="item-head"><span class="item-name">Organic Earl Grey Tea</span><span class="item-price">$5.00</span></div>
      <p class="item-desc">Small $5 - Medium $6 - Large $7</p>
    </div>
    <div class="item" style="top:403px;">
      <div class="item-head"><span class="item-name">Hot Chocolate</span><span class="item-price">$5.00</span></div>
      <p class="item-desc">Small $5 - Medium $6 - Large $7</p>
    </div>
    <div class="item" style="top:460px;">
      <div class="item-head"><span class="item-name">Dark Cacoa Hot Chocolate</span><span class="item-price">$5.00</span></div>
      <p class="item-desc">Small $5 - Medium $6 - Large $7</p>
    </div>
    <div class="item" style="top:515px;">
      <div class="item-head"><span class="item-name">Chai Latte</span><span class="item-price">$5.00</span></div>
      <p class="item-desc" style="margin-top:1px;">Small $5 - Medium $6 - Large $7</p>
    </div>

    <div class="rule" style="left:427px; top:568px; width:308px;"></div>

    <div class="item" style="top:587px;">
      <div class="item-head"><span class="item-name">RAW Natural Infusions</span><span class="item-price">$0.50</span></div>
      <p class="item-desc">Caramel, Vanilla, Chai Spice,<br>Hazelnut, Belgian Chocolate</p>
    </div>
    <div class="item" style="top:668px;">
      <div class="item-head"><span class="item-name">Milks</span><span class="item-price">$INC</span></div>
      <p class="item-desc">Full Cream, Skinny, Oat,<br>Almond, Soy</p>
    </div>
  </section>

  <div class="rule" style="left:43px; top:787px; width:692px;"></div>

  <section>
    <h2 class="specials-title">Specialty Drinks</h2>

    <div class="special" style="top:897px;">
      <h3 class="special-name">Honey Brewed Chai</h3>
      <p class="special-desc">Our Honey Chai Is Handmade And Blended In Western Australia. It Is Made From The Finest Black Tea Leaves<br>Available, Aromatic Freshly Ground Spices And Infused With Locally Sourced Raw Honey.<br>Served With A Choice Of Steamed Milk</p>
      <p class="special-price">$7.00</p>
    </div>

    <div class="special" style="top:1019px; left:40px; width:697px;">
      <h3 class="special-name">Colombian Cacoa Salted Caramel Hot Chocolate</h3>
      <p class="special-desc">Made With Deep Toned And Rich Cocoa Sourced From Ancient Cocao Growing Regions Of Colombia And Sweetened<br>With Just Enough Organic Unrefined Colombian Panela, All Balanced Perfectly With A Caramel Raw Natural Infusion<br>And Pink Himalayan Rock Salt. Served With A Choice Of Steamed Milk</p>
      <p class="special-price">$7.00</p>
    </div>
  </section>

  <div class="rule" style="left:43px; top:1159px; width:692px;"></div>
</main>
</body>
</html>
```